Website Homepage Redesign - make it pretty and bold

I have a website (www.pravelle.com) which is hosted through Shopify. I want to redesign my homepage with a new theme which includes: photos of kids wearing my jewellery, category placeholders, Instagram feed and what's new. New colours on the homepage is a mix of pink and white so my brand will be more appealing to girls. I want the redesign to be a big step forward for my brand, so anyone who looks at my website will go “wow I must buy this”. I have some photos already (attached below), I will be getting a few more soon. I am thinking a colour scheme of light pink, rose and white. I was thinking the Shopify theme of “flint” or “marigolda” or something similar. I will purchase from theme in shopify once agreed.The second page, would be a Category page, which I could visually show the different categories I have, either shop by theme (ie. Unicorns, under the sea, angels), or by type (eg. rings, necklace) but it would be simple and clean page. It would be a mix of photos with text on the top, and colour blocks with text.

Target Market(s)

Women aged 20 - 45 with a daughter (aged baby to 12) based in Australia

Industry/Entity Type

Jewelry

Number of Pages Required

2 page

Font styles to use
Sans Serif

Colors
f59195
fbd4d5
feeeee

Requirements
Must have
• Page 1: Logo, main hero photo section (sliding), category links, what's new section, Instagram feed, payment types, newsletter signup
• Page 2: category page with imagery and clickable photos
• I will be the one who is going to update the website after handover, so no crazy fonts that I have to buy.
• I want it to work with Shopify, so I prefer a theme that I can update easily.
• My Instagram is: www.snapvista/pravellekidz
Nice to have
• Other suggestions from the designer are welcome
Should not have
• I'm not very good at my blog, so not interested in pushing this.
• I like my logo, I'm not interested in changing it.

```html
<!DOCTYPE html>
<html lang="en">
<head>
<meta charset="utf-8">
<title>Pravelle — Jewellery for Little Girls</title>
<link href="https://fonts.googleapis.com/css2?family=Montserrat:wght@300;400;500;600;700&family=Open+Sans:wght@400;600;700&display=swap" rel="stylesheet">
<style>
:root{
  --rose:#f59195;
  --rose-deep:#ee7f84;
  --blush:#fbd4d5;
  --petal:#feeeee;
  --ink:#333;
  --muted:#8a8a8a;
  --line:#e4e4e4;
  --footer:#222224;
  --white:#fff;
}
*{box-sizing:border-box;margin:0;padding:0}
html,body{width:1200px;height:4534px;overflow:hidden}
body{position:relative;background:var(--white);font-family:"Open Sans",sans-serif;color:var(--ink)}
.abs{position:absolute}
.wrap{left:85px;width:1030px}

/* top bar */
.topbar{top:0;left:0;width:1200px;height:45px;background:var(--rose);color:var(--white);font-size:10px;font-weight:600;letter-spacing:.3px;display:flex;align-items:center;justify-content:space-between;padding:0 88px}
.topbar .links span{margin-left:14px}

/* header */
.header{top:45px;height:140px;display:flex;align-items:center;justify-content:space-between}
.account{font-size:11px;font-weight:600;width:300px}
.account span{margin-right:10px}
.brand{font-family:"Montserrat",sans-serif;font-weight:700;font-size:46px;color:var(--rose);letter-spacing:-.5px}
.search{width:310px;height:38px;border:1px solid #cfcfcf;display:flex;align-items:center;justify-content:space-between;padding:0 12px;font-size:11px;color:#666}
.nav{top:178px;height:36px;display:flex;justify-content:center;gap:52px;font-size:11px;font-weight:600;font-family:"Montserrat",sans-serif;align-items:center}

/* hero */
.hero{top:227px;height:508px;background:linear-gradient(100deg,#d9a48e 0%,#e9c3b3 35%,#c9c6cc 65%,#b6b8c4 100%)}
.hero-copy{position:absolute;left:560px;top:130px;width:400px;color:var(--white)}
.hero-copy .brand{color:var(--white);font-size:78px;display:block;margin-bottom:14px}
.hero-copy p{font-size:11px;line-height:22px}
.btn{display:inline-block;background:var(--rose);color:var(--white);font-family:"Montserrat",sans-serif;font-size:12px;font-weight:600;padding:12px 32px;border-radius:30px;letter-spacing:.5px}
.hero-copy .btn{margin-top:24px}
.dots{position:absolute;right:50px;bottom:16px;display:flex;gap:6px}
.dots i{width:9px;height:9px;border-radius:50%;background:var(--white);display:block}
.dots i:first-child{background:var(--rose)}

/* promos */
.promo{top:750px;width:505px;height:287px}
.promo.earrings{left:85px;background:linear-gradient(90deg,#c2b4ae,#ddd3ce)}
.promo.bracelets{left:608px;background:linear-gradient(90deg,#f2b3b7,#f7c9cb)}
.promo-copy{position:absolute;top:78px;width:200px}
.promo.earrings .promo-copy{left:278px}
.promo.bracelets .promo-copy{left:30px}
.promo h3{font-family:"Montserrat",sans-serif;font-weight:400;font-size:30px;letter-spacing:1.5px;color:#444}
.promo p{font-size:10px;line-height:18px;color:#555;margin:8px 0 16px}
.btn-outline{display:inline-block;border:1px solid #555;font-size:10px;font-weight:600;padding:8px 18px;color:#444}

/* section titles */
.title{left:0;width:1200px;text-align:center;font-family:"Montserrat",sans-serif;font-weight:400;font-size:32px;letter-spacing:1.5px;color:#444}
.title::after{content:"";display:block;width:90px;height:2px;background:var(--rose);margin:12px auto 0}

/* categories */
.cats{top:1167px;display:flex;gap:10px}
.cat{width:250px;text-align:center}
.cat .ph{height:248px;border:1px solid var(--line)}
.cat h4{font-size:16px;font-weight:400;margin-top:22px;color:#444}
.cat .price{font-size:15px;color:var(--rose);margin-top:6px}
.cat .price s{color:var(--muted)}
.arrow{top:1270px}

/* about */
.about{top:1520px;height:433px;background:linear-gradient(120deg,#e9a2a5,#f4bfc0 50%,#e79aa0);text-align:center;color:var(--white);padding-top:100px}
.about h2{font-family:"Montserrat",sans-serif;font-weight:700;font-size:56px;letter-spacing:1px}
.about p{font-size:14px;line-height:30px;font-weight:600;width:700px;margin:12px auto 32px}
.btn-ghost{display:inline-block;border:2px solid var(--white);border-radius:30px;padding:13px 44px;font-family:"Montserrat",sans-serif;font-size:13px;font-weight:600;letter-spacing:1px}

/* reviews */
.reviews{top:2083px;display:flex;gap:20px}
.review{width:330px}
.review .box{height:190px;border:1px solid var(--line);padding:18px 24px;font-size:11px;line-height:21px;color:#777}
.stars{color:var(--rose);font-size:15px;letter-spacing:1px;margin-bottom:8px;font-weight:700}
.stars b{color:#555;margin-right:6px;font-size:22px;vertical-align:-4px}
.person{display:flex;align-items:center;margin-top:28px;gap:14px}
.avatar{width:60px;height:60px;border-radius:50%;background:linear-gradient(135deg,#d7a88e,#9b7765)}
.person h5{font-size:12px;font-weight:700;letter-spacing:.5px}
.person small{font-size:10px;color:var(--muted)}

/* news banner */
.news{top:2421px;height:436px;background:linear-gradient(90deg,#e9b9a9 0%,#d9b3b2 45%,#cfa7ad 100%)}
.news-copy{position:absolute;left:508px;top:112px;width:420px;color:var(--white)}
.news-copy h2{font-family:"Montserrat",sans-serif;font-weight:600;font-size:42px;letter-spacing:1px}
.news-copy p{font-size:11px;line-height:22px;margin:14px 0 26px}

/* latest news */
.posts{top:2987px;display:flex;gap:15px}
.post{width:333px;height:432px;border:1px solid var(--line);text-align:center}
.post .ph{height:229px}
.post h4{font-size:13px;font-weight:700;margin-top:28px;letter-spacing:.4px}
.post .date{font-size:12px;color:var(--rose);margin:10px 0 12px;display:flex;justify-content:center;align-items:center;gap:8px}
.post p{font-size:10.5px;line-height:20px;color:#777;padding:0 26px}

/* instagram */
.insta{top:3543px;display:flex;gap:14px}
.insta .ph{width:195px;height:184px}

/* newsletter */
.newsletter{top:3779px;left:0;width:1200px;height:317px;background:var(--rose);text-align:center;color:var(--white)}
.newsletter h2{font-family:"Montserrat",sans-serif;font-weight:400;font-size:32px;letter-spacing:2px;margin-top:40px}
.newsletter p{font-size:11px;line-height:22px;width:700px;margin:20px auto 26px}
.signup{display:flex;width:656px;height:46px;margin:0 auto}
.signup .field{flex:1;background:var(--white);color:#666;font-size:12px;text-align:left;padding:15px 18px}
.signup .go{width:120px;background:#444;color:var(--white);font-size:12px;font-weight:700;padding-top:15px}

/* footer */
.footer{top:4096px;left:0;width:1200px;height:438px;background:var(--footer);color:#ddd}
.footer .brand{position:absolute;left:115px;top:128px;font-size:44px;color:var(--rose)}
.fcol{position:absolute;top:56px;font-size:11px}
.fcol h6{font-family:"Montserrat",sans-serif;font-size:14px;font-weight:600;color:var(--white);margin-bottom:14px;letter-spacing:.5px}
.fcol li{list-style:none;line-height:24px}
.fcol li::before{content:"›";margin-right:12px;color:#aaa}
.fcol.contact li::before{content:none}
.fcol.contact li{display:flex;gap:10px;align-items:flex-start;line-height:20px;margin-bottom:6px}
.fcol.contact a{color:var(--white)}
.social{position:absolute;top:212px;left:0;width:1200px;display:flex;justify-content:center;gap:8px}
.social i{width:30px;height:30px;border:1.5px solid #ddd;border-radius:50%;display:block}
.pay{position:absolute;top:262px;left:0;width:1200px;display:flex;justify-content:center;gap:6px}
.pay i{width:40px;height:24px;border-radius:3px;display:block}
.copy{position:absolute;top:395px;left:0;width:1200px;text-align:center;font-size:11px}
</style>
</head>
<body>

<div class="abs topbar">
  <span>SELECT CURRENCY: USD ⌄</span>
  <span>FREE SHIPPING FOR ORDERS OVER $60 AUD AND $100 US, UK, NZ)</span>
  <span class="links"><span>🛒 CART (0)</span><span>|</span><span>CHECKOUT</span></span>
</div>

<header class="abs wrap header">
  <div class="account"><span>LOG IN</span><span>|</span><span>SIGN UP</span></div>
  <div class="brand">Pravelle</div>
  <div class="search"><span>SEARCH</span>
    <svg width="13" height="13" viewBox="0 0 14 14"><circle cx="6" cy="6" r="4.5" fill="none" stroke="#444" stroke-width="1.6"/><line x1="9.3" y1="9.3" x2="13" y2="13" stroke="#444" stroke-width="1.6"/></svg>
  </div>
</header>

<nav class="abs wrap nav">
  <span>HOME</span><span>SHOP</span><span>REVIEWS</span><span>ABOUT US</span><span>FAQ'S</span><span>STORE POLICIES</span><span>BLOG</span><span>MEDIA</span><span>CONTACT US</span>
</nav>

<section class="abs wrap hero" role="img" aria-label="Photo of a young girl in a sun hat wearing a bracelet on the beach">
  <div class="hero-copy">
    <span class="brand">Pravelle</span>
    <p>Sed ut perspiciatis unde omnis iste natus error sit voluptatem accusan tium doloremque laudantium, totam rem aperiam, eaque ipsa quae ab illo inventore veritatis et quasi architecto beatae vitae dicta sunt explicabo.</p>
    <span class="btn">READ MORE</span>
  </div>
  <div class="dots"><i></i><i></i><i></i></div>
</section>

<section class="abs promo earrings" role="img" aria-label="Photo of sparkling crystal stud earrings">
  <div class="promo-copy"><h3>EARRINGS</h3><p>Sed ut perspiciatis unde omnis iste natus error sit voluptatem accusantium</p><span class="btn-outline">VIEW MORE</span></div>
</section>
<section class="abs promo bracelets" role="img" aria-label="Photo of a pink charm bracelet">
  <div class="promo-copy"><h3>BRACELETS</h3><p>Sed ut perspiciatis unde omnis iste natus error sit voluptatem accusantium</p><span class="btn-outline">VIEW MORE</span></div>
</section>

<h2 class="abs title" style="top:1086px">OUR CATEGORY</h2>

<svg class="abs arrow" style="left:42px" width="18" height="60" viewBox="0 0 18 60"><polyline points="16,2 2,30 16,58" fill="none" stroke="#bbb" stroke-width="1.5"/></svg>
<svg class="abs arrow" style="left:1140px" width="18" height="60" viewBox="0 0 18 60"><polyline points="2,2 16,30 2,58" fill="none" stroke="#bbb" stroke-width="1.5"/></svg>

<div class="abs wrap cats">
  <div class="cat"><div class="ph" role="img" aria-label="Product photo of a black owl charm" style="background:linear-gradient(#f6f6f6,#e9e9e9)"></div><h4>Black Owl</h4><div class="price">$9.00</div></div>
  <div class="cat"><div class="ph" role="img" aria-label="Product photo of a leather bracelet" style="background:linear-gradient(#f7f3f4,#ece3e6)"></div><h4>Leather Bracelet</h4><div class="price">$15.00</div></div>
  <div class="cat"><div class="ph" role="img" aria-label="Product photo of pink love heart stud earrings" style="background:linear-gradient(#f8f4f6,#ede6ea)"></div><h4>Love Stud Earrings</h4><div class="price">$18.00–<s>$22.00</s></div></div>
  <div class="cat"><div class="ph" role="img" aria-label="Product photo of a dried flower pendant necklace" style="background:linear-gradient(#f7f7f3,#ecebe3)"></div><h4>Dried Flower Necklace</h4><div class="price">$9.00</div></div>
</div>

<section class="abs wrap about" role="img" aria-label="Photo of pink sprinkles and cupcakes">
  <h2>ABOUT US</h2>
  <p>Pravelle Pty Ltd (pronounced "Pra - vel") is a Sydney-based company that loves all things that glow in the sun, that are just too cute and fluffy to resist. Pravelle is a fun, kid friendly spot for jewellery.</p>
  <span class="btn-ghost">SHOP NOW</span>
</section>

<h2 class="abs title" style="top:1996px">OUR REVIEWS</h2>

<div class="abs wrap reviews">
  <div class="review"><div class="box"><div class="stars"><b>❝</b>★★★★★</div>Sed ut perspiciatis unde omnis iste natus error sit voluptatem accusantium doloremque laudantium, totam rem aperiam, eaque ipsa quae ab illo inventore veritatis et quasi architecto beatae vitae dicta sunt explicabo.</div>
    <div class="person"><div class="avatar" role="img" aria-label="Customer portrait"></div><div><h5>MARA ELLISON</h5><small>Posted on August 21, 2019</small></div></div></div>
  <div class="review"><div class="box"><div class="stars"><b>❝</b>★★★★★</div>Sed ut perspiciatis unde omnis iste natus error sit voluptatem accusantium doloremque laudantium, totam rem aperiam, eaque ipsa quae ab illo inventore veritatis et quasi architecto beatae vitae dicta sunt explicabo.</div>
    <div class="person"><div class="avatar" role="img" aria-label="Customer portrait"></div><div><h5>RHEA COSTAIN</h5><small>Posted on July 30, 2019</small></div></div></div>
  <div class="review"><div class="box"><div class="stars"><b>❝</b>★★★★★</div>Sed ut perspiciatis unde omnis iste natus error sit voluptatem accusantium doloremque laudantium, totam rem aperiam, eaque ipsa quae ab illo inventore veritatis et quasi architecto beatae vitae dicta sunt explicabo.</div>
    <div class="person"><div class="avatar" role="img" aria-label="Customer portrait"></div><div><h5>LENA WHITCOMBE</h5><small>Posted on June 10, 2019</small></div></div></div>
</div>

<section class="abs wrap news" role="img" aria-label="Photo of a little girl in a lilac dress wearing a pendant">
  <div class="news-copy">
    <h2>IN THE NEWS</h2>
    <p>Pravelle Pty Ltd (pronounced "Pra - vel") is a Sydney-based company that loves all things that glow in the sun, that are just too cute and fluffy to resist. Pravelle is a fun, kid friendly spot for jewellery.</p>
    <span class="btn">SHOP NOW</span>
  </div>
</section>

<h2 class="abs title" style="top:2900px">LATEST NEWS</h2>

<div class="abs wrap posts">
  <article class="post"><div class="ph" role="img" aria-label="Photo of donuts and a bracelet on a pink table" style="background:linear-gradient(135deg,#f3c7cf,#e6d6c8)"></div><h4>SED UT PERSPICIATIS UNDE</h4>
    <div class="date"><svg width="12" height="12" viewBox="0 0 12 12"><rect x="1" y="2" width="10" height="9" fill="none" stroke="#f59195"/><line x1="1" y1="5" x2="11" y2="5" stroke="#f59195"/></svg>JUNE 20, 2019</div>
    <p>Nemo enim ipsam voluptatem quia voluptas sit aspernatur aut odit aut fugit, sed quia consequuntur magni dolores eos qui ratione voluptatem sequi nesciunt.</p></article>
  <article class="post"><div class="ph" role="img" aria-label="Photo of a child's wrist wearing a charm bracelet" style="background:linear-gradient(135deg,#e69aa6,#3a3030)"></div><h4>SED UT PERSPICIATIS UNDE</h4>
    <div class="date"><svg width="12" height="12" viewBox="0 0 12 12"><rect x="1" y="2" width="10" height="9" fill="none" stroke="#f59195"/><line x1="1" y1="5" x2="11" y2="5" stroke="#f59195"/></svg>JUNE 20, 2019</div>
    <p>Nemo enim ipsam voluptatem quia voluptas sit aspernatur aut odit aut fugit, sed quia consequuntur magni dolores eos qui ratione voluptatem sequi nesciunt.</p></article>
  <article class="post"><div class="ph" role="img" aria-label="Photo of a girl in a white top wearing a pendant" style="background:linear-gradient(135deg,#cfd3db,#efece8)"></div><h4>SED UT PERSPICIATIS UNDE</h4>
    <div class="date"><svg width="12" height="12" viewBox="0 0 12 12"><rect x="1" y="2" width="10" height="9" fill="none" stroke="#f59195"/><line x1="1" y1="5" x2="11" y2="5" stroke="#f59195"/></svg>JUNE 20, 2019</div>
    <p>Nemo enim ipsam voluptatem quia voluptas sit aspernatur aut odit aut fugit, sed quia consequuntur magni dolores eos qui ratione voluptatem sequi nesciunt.</p></article>
</div>

<h2 class="abs title" style="top:3463px">INSTAGRAM</h2>

<div class="abs wrap insta">
  <div class="ph" role="img" aria-label="Feed photo of a girl in a sun hat" style="background:linear-gradient(135deg,#d9ad94,#b9c2cc)"></div>
  <div class="ph" role="img" aria-label="Feed photo of a bracelet with red roses" style="background:linear-gradient(135deg,#f1c9c9,#c73b48)"></div>
  <div class="ph" role="img" aria-label="Feed photo of a girl wearing a pendant" style="background:linear-gradient(135deg,#c9c7dc,#e7e2ee)"></div>
  <div class="ph" role="img" aria-label="Feed photo of a straw hat and jewellery" style="background:linear-gradient(135deg,#d8b79a,#e8b8c4)"></div>
  <div class="ph" role="img" aria-label="Feed photo of donuts and sprinkles" style="background:linear-gradient(135deg,#f4c6cf,#d2607a)"></div>
</div>

<section class="abs newsletter">
  <h2>NEWSLETTER</h2>
  <p>Sed ut perspiciatis unde omnis iste natus error sit voluptatem accusantium doloremque laudantium, totam rem aperiam, eaque ipsa quae ab illo inventore veritatis et quasi architecto beatae vitae dicta sunt explicabo.</p>
  <div class="signup"><div class="field">Enter Your Email</div><div class="go">SUBSCRIBE</div></div>
</section>

<footer class="abs footer">
  <div class="brand">Pravelle</div>
  <div class="fcol" style="left:345px"><h6>INFORMATION</h6><ul><li>Sitemap</li><li>Shipping &amp; Returns</li><li>Privacy Notice</li><li>Conditions of Use</li><li>About us</li><li>Contact us</li></ul></div>
  <div class="fcol" style="left:532px"><h6>CUSTOMER SERVICE</h6><ul><li>Search</li><li>Blog</li><li>Recently viewed products</li><li>Compare products list</li><li>New products</li></ul></div>
  <div class="fcol" style="left:755px"><h6>MY ACCOUNT</h6><ul><li>My account</li><li>Orders</li><li>Addresses</li><li>Shopping cart</li><li>Wishlist</li></ul></div>
  <div class="fcol contact" style="left:920px"><h6>CONTACT US</h6><ul>
    <li><svg width="12" height="12" viewBox="0 0 12 12"><path d="M2 1h3l1 3-2 1a7 7 0 0 0 3 3l1-2 3 1v3c-6 0-9-3-9-9z" fill="#ddd"/></svg>(000) 555-0142 (Phone)</li>
    <li><svg width="12" height="12" viewBox="0 0 12 12"><rect x="1" y="3" width="10" height="7" fill="#ddd"/><rect x="3" y="1" width="6" height="3" fill="#ddd"/></svg>(000) 555-0143 (Fax)</li>
    <li><svg width="12" height="12" viewBox="0 0 12 12"><rect x="1" y="2.5" width="10" height="7" fill="none" stroke="#ddd"/><polyline points="1,3 6,7 11,3" fill="none" stroke="#ddd"/></svg><a>hello@pravelle.com</a></li>
    <li><svg width="12" height="14" viewBox="0 0 12 14"><path d="M6 13C2 8 1 6 1 5a5 5 0 0 1 10 0c0 1-1 3-5 8z" fill="#ddd"/><circle cx="6" cy="5" r="1.8" fill="#222"/></svg>#1402 Lorem Ipsum Dummy<br>Text Lorem Ipsum</li>
  </ul></div>
  <div class="social"><i></i><i></i><i></i><i></i><i></i></div>
  <div class="pay"><i style="background:#e9e9e9"></i><i style="background:#d9d9d9"></i><i style="background:#cfe0ef"></i><i style="background:#e3e3e3"></i><i style="background:#d6d6d6"></i></div>
  <div class="copy">© Copyright 2019 Pravelle. All Rights Reserved</div>
</footer>

</body>
</html>
```